<作成物>
■リッチメッセージ
リッチメニュー
合計2枚
リッチメニュー の表示項目は画像写真添付します。
写真添付しております。

【デザインの詳細】
オレンジ(画像の女性のエプロンのオレンジと似せてください)
をベースに元気でハッピーになれるような感じを希望しております。
使用される画像は添付のアドレスに入ってりますの
でどれを使用されても構いません。
イメージのデザイン合わせた感じにしていただけると嬉しいです。
https://files.tovrelink-share.example/dl/5k2m9q7x3c8v1b4n6z0p
上下で一体感があるものを希望します。
人物の画像は入れても入れなくても(デザインで決めてください)

【表示文言】
上の画像に入れる文言
工作感覚で作るから初めてでも大丈夫!
可愛い過ぎるお寿司レッスン
(文字がデザイン的に合わなければ入れなくてもOK)

〈リッチメニューの表示項目〉
画像の中に入れますの、これを参考に入れてください。

デザイン重視でここの表示名はデザイン的に英語の方がよければ
英語でも大丈夫です。意味がわかって
ニュアンスがあっていれば文字を短くするのも
お任せします。あくまでデザイン重視です。
〈画像はこちらから〉
画像

※こちらの作成以外に勝手に使用された場合は
著作権侵害で法的手段をとらせていただきます。
作成事例にもしようしないでください。

<サイズ>
・リッチメッセージ(1040×1040ピクセル)
・リッチメニュー(1200×810ピクセル)

<納品形式>
・ai形式(イラストレーターデータ)
・JPG
<詳細>
※添付ファイルをご確認ください。

<備考>
ブランディング効果を期待しています。
どんどん何個でも応募ください。

```html
<!DOCTYPE html>
<html lang="ja">
<head>
<meta charset="utf-8">
<title>可愛い過ぎるお寿司レッスン</title>
<link rel="stylesheet" href="https://fonts.googleapis.com/css2?family=M+PLUS+Rounded+1c:wght@500;700;800;900&family=Kalam:wght@700&display=swap">
<style>
  :root{
    --orange:#f39a2b;
    --orange-deep:#ec8519;
    --cream:#fff8e8;
    --brown:#5a3218;
    --red:#e5452c;
    --ink:#2b1d14;
    --white:#ffffff;
  }
  *{margin:0;padding:0;box-sizing:border-box}
  html,body{width:717px;height:1200px;overflow:hidden;background:var(--cream)}
  .menu-card{position:relative;width:717px;height:1200px;overflow:hidden;background:var(--cream);font-family:"M PLUS Rounded 1c",sans-serif}

  .hero-photos{position:absolute;left:0;top:0;width:717px;height:560px;z-index:0;
    background:linear-gradient(135deg,#7a4a2b 0%,#c98a4a 30%,#e9c88a 55%,#8d5a32 80%,#5e3a20 100%)}
  .presenter-photo{position:absolute;left:565px;top:470px;width:152px;height:230px;z-index:1;
    background:linear-gradient(180deg,#f6e6d6 0%,#f4b070 60%,var(--orange) 100%)}

  .title-badge{position:absolute;left:148px;top:32px;width:420px;height:420px;z-index:2}
  .title-badge svg{position:absolute;inset:0}
  .title-ribbon{position:absolute;left:100px;top:58px;width:220px;height:50px;border-radius:25px;
    background:var(--orange);color:var(--white);font-weight:800;font-size:28px;
    display:flex;align-items:center;justify-content:center;letter-spacing:1px}
  .title-main{position:absolute;left:0;width:420px;text-align:center;color:var(--brown);font-weight:900;line-height:1;white-space:nowrap}
  .title-main.line-1{top:130px;font-size:100px}
  .title-main.line-1 .accent{color:var(--red)}
  .title-main.line-2{top:252px;font-size:76px;letter-spacing:-2px}
  .mascot{position:absolute;width:92px;height:118px;border-radius:46% 46% 40% 40%;z-index:3;
    background:linear-gradient(180deg,#6b4a2e,#e6a94e)}
  .mascot.left{left:60px;top:265px}
  .mascot.right{left:548px;top:265px}

  .tagline-band{position:absolute;left:0;top:552px;width:440px;height:42px;background:var(--orange);z-index:4;
    color:var(--white);font-family:"Kalam",cursive;font-size:24px;padding-left:22px;line-height:46px;white-space:nowrap}
  .lead{position:absolute;left:34px;top:606px;width:540px;text-align:left;color:var(--orange-deep);z-index:4;
    font-weight:800;font-size:37px;line-height:50px;white-space:nowrap}

  .menu-grid{position:absolute;left:20px;top:736px;width:677px;height:440px;
    display:grid;grid-template-columns:repeat(3,213px);grid-template-rows:repeat(2,212px);gap:16px 19px}
  .menu-tile{position:relative;display:flex;flex-direction:column;align-items:center;justify-content:center;text-align:center}
  .menu-tile svg.frame{position:absolute;inset:0;width:100%;height:100%}
  .menu-tile .label-en{position:relative;color:var(--orange-deep);font-weight:900;font-size:40px;line-height:1.05}
  .menu-tile .label-en.small{font-size:32px}
  .menu-tile .label-jp{position:relative;color:var(--ink);font-weight:700;font-size:21px;margin-top:6px}
  .sns-dots{position:relative;display:flex;gap:8px;margin-top:8px}
  .sns-dots span{width:20px;height:20px;border-radius:4px;background:var(--ink)}
</style>
</head>
<body>
<svg width="0" height="0" style="position:absolute">
  <defs>
    <path id="scallop" d="M15 15 a15 12 0 0 1 30 0 a15 12 0 0 1 30 0 a15 12 0 0 1 30 0 a15 12 0 0 1 30 0 a15 12 0 0 1 30 0 a15 12 0 0 1 30 0 a12 15 0 0 1 0 30 a12 15 0 0 1 0 30 a12 15 0 0 1 0 30 a12 15 0 0 1 0 30 a12 15 0 0 1 0 30 a12 15 0 0 1 0 30 a15 12 0 0 1 -30 0 a15 12 0 0 1 -30 0 a15 12 0 0 1 -30 0 a15 12 0 0 1 -30 0 a15 12 0 0 1 -30 0 a15 12 0 0 1 -30 0 a12 15 0 0 1 0 -30 a12 15 0 0 1 0 -30 a12 15 0 0 1 0 -30 a12 15 0 0 1 0 -30 a12 15 0 0 1 0 -30 a12 15 0 0 1 0 -30 Z"/>
  </defs>
</svg>

<main class="menu-card">
  <div class="hero-photos" role="img" aria-label="飾り巻き寿司の写真コラージュ"></div>
  <div class="presenter-photo" role="img" aria-label="オレンジのエプロン姿の講師と花の飾り寿司の写真"></div>

  <div class="title-badge">
    <svg viewBox="0 0 420 420">
      <circle cx="210" cy="210" r="206" fill="var(--orange)"/>
      <circle cx="210" cy="210" r="192" fill="var(--cream)"/>
      <circle cx="210" cy="210" r="182" fill="none" stroke="var(--orange)" stroke-width="2" stroke-dasharray="6 6"/>
    </svg>
    <div class="title-ribbon">可愛い過ぎる</div>
    <div class="title-main line-1">お寿<span class="accent">司</span></div>
    <div class="title-main line-2">レッスン</div>
  </div>
  <div class="mascot left" role="img" aria-label="動物の顔の飾り巻き寿司イラスト"></div>
  <div class="mascot right" role="img" aria-label="鳥の形の飾り巻き寿司イラスト"></div>

  <div class="tagline-band">Even beginners can enjoy! ♡</div>
  <p class="lead">工作感覚で作れるから<br>初めての方でも大丈夫です!</p>

  <nav class="menu-grid">
    <a class="menu-tile"><svg class="frame" viewBox="0 0 210 210" preserveAspectRatio="none"><use href="#scallop" fill="var(--white)" stroke="var(--ink)" stroke-width="2"/></svg><span class="label-en">Menu</span><span class="label-jp">お寿司</span></a>
    <a class="menu-tile"><svg class="frame" viewBox="0 0 210 210" preserveAspectRatio="none"><use href="#scallop" fill="var(--white)" stroke="var(--ink)" stroke-width="2"/></svg><span class="label-en small">Schedule</span><span class="label-jp">空席状況</span></a>
    <a class="menu-tile"><svg class="frame" viewBox="0 0 210 210" preserveAspectRatio="none"><use href="#scallop" fill="var(--white)" stroke="var(--ink)" stroke-width="2"/></svg><span class="label-en">Event</span><span class="label-jp">イベント</span></a>
    <a class="menu-tile"><svg class="frame" viewBox="0 0 210 210" preserveAspectRatio="none"><use href="#scallop" fill="var(--white)" stroke="var(--ink)" stroke-width="2"/></svg><span class="label-en">Web</span><span class="label-jp">ホームページ</span></a>
    <a class="menu-tile"><svg class="frame" viewBox="0 0 210 210" preserveAspectRatio="none"><use href="#scallop" fill="var(--white)" stroke="var(--ink)" stroke-width="2"/></svg><span class="label-en">SNS</span><span class="sns-dots"><span></span><span></span><span></span></span></a>
    <a class="menu-tile"><svg class="frame" viewBox="0 0 210 210" preserveAspectRatio="none"><use href="#scallop" fill="var(--white)" stroke="var(--ink)" stroke-width="2"/></svg><span class="label-en small">Online<br>Lesson</span><span class="label-jp">対面レッスン</span></a>
  </nav>
</main>
</body>
</html>
```